Billboard design for a jewelry store.

I am looking for a very unique design with a catchy slogan, I am looking for billboard so good that will make the front page of the newspaper. I want to target customers that are looking for diamond jewelry or diamonds in general. For sure not interested in anything that is genetic or been used in the past. I want the billboard to stand out and very unique. Text not more than 3 words, our logo and an image.

Target Market(s)

Local

Industry/Entity Type

Jewelry Store

Font styles to use
Other font styles liked:
• Open to your suggestion for the font.

Requirements
Must have
• Unique, very brief a catchy slogan. My logo and an image. Open for suggestions. I want also different formats to use on social media.
Nice to have
• I am open to unique and amazing new ideas. I don't want general used design or slogan.
Should not have
• Too much text

```html
<!DOCTYPE html>
<html lang="en">
<head>
<meta charset="UTF-8">
<title>Varro Jewelers Billboard</title>
<link href="https://fonts.googleapis.com/css2?family=Dancing+Script:wght@500&family=Cinzel:wght@700&display=swap" rel="stylesheet">
<style>
  :root {
    --stage: #b9cfdf;
    --board: #000000;
    --stone-light: #5a5a60;
    --stone-mid: #35353a;
    --stone-dark: #1a1a1d;
    --gem-core: #ffffff;
    --gem: #dfe3ec;
    --gem-edge: #9aa0ad;
    --ink: #ffffff;
  }
  html, body {
    margin: 0;
    padding: 0;
    width: 1200px;
    height: 800px;
    overflow: hidden;
    background: var(--stage);
  }
  .canvas {
    position: relative;
    width: 1200px;
    height: 800px;
  }
  .billboard {
    position: absolute;
    left: 40px;
    top: 225px;
    width: 1120px;
    height: 350px;
    background: var(--board);
    overflow: hidden;
  }
  .hero-image {
    position: absolute;
    left: 0;
    top: 0;
    width: 600px;
    height: 350px;
    background:
      radial-gradient(ellipse 130px 95px at 210px 150px, var(--gem-core) 0%, var(--gem) 35%, var(--gem-edge) 70%, rgba(154,160,173,0) 100%),
      radial-gradient(ellipse 420px 330px at 220px 250px, var(--stone-light) 0%, var(--stone-mid) 45%, var(--stone-dark) 78%, var(--board) 100%);
  }
  .slogan {
    position: absolute;
    left: 610px;
    width: 440px;
    top: 72px;
    margin: 0;
    text-align: center;
    font-family: "Dancing Script", cursive;
    font-weight: 500;
    font-size: 56px;
    line-height: 68px;
    color: var(--ink);
  }
  .brand-name {
    position: absolute;
    left: 610px;
    width: 440px;
    top: 268px;
    margin: 0;
    text-align: center;
    font-family: "Cinzel", serif;
    font-weight: 700;
    font-size: 24px;
    letter-spacing: 3px;
    color: var(--ink);
  }
</style>
</head>
<body>
  <div class="canvas">
    <section class="billboard">
      <div class="hero-image" role="img" aria-label="Photograph of a large brilliant-cut diamond resting on a dark rough stone"></div>
      <h1 class="slogan">Ultimate<br>Luxury &amp; Style</h1>
      <p class="brand-name">Varro Jewelers</p>
    </section>
  </div>
</body>
</html>
```